Website art for a private investigator.

The purposed graphic is for a business website ( dorvelgrp.example ). The business name is “Dorvale & Kestrin ltd.” This firm is a private investigation agency. The purposed graphic will be placed in the upper most main area of the main page of the website. If you look at the website now there is no graphic.

I have an idea of what I am looking for. I imagine a graphic depicting a contemporary private investigator walking through a dark alley searching for some unknown item. This is symbolic of private investigators hired to find information for people who their selfs do not have the know how nor could they handle the complexity and high stress environment. When I say contemporary I am referring to todays private investigators typically highly educated and well dressed.

Target Market(s)

People who need a private investigator

Industry/Entity Type

Business

Requirements
Must have
• match website; I have an idea of what I am looking for. I imagine a graphic depicting a contemporary private investigator walking through a dark alley searching for some unknown item. This is symbolic of private investigators hired to find information for people who their selfs do not have the know how nor could they handle the complexity and high stress environment. When I say contemporary I am referring to todays private investigators typically highly educated and well dressed.
Should not have
• Everyone please understand, I am not looking for a new website. I am only looking for the image. If you have submitted a design and its displayed on another website other than mine. I will not select your design. I am sorry for being harsh, but I asked for the image to match my website.

```html
<!DOCTYPE html>
<html lang="en">
<head>
<meta charset="utf-8">
<title>Dorvale &amp; Kestrin ltd. — Private Investigation and Analysis</title>
<link rel="stylesheet" href="https://fonts.googleapis.com/css2?family=Lato:ital,wght@0,400;0,700;1,400;1,700&family=Montserrat:wght@400;600;700&display=swap">
<style>
:root{
  --ink:#1d1d1d;
  --body:#3a3a3a;
  --muted:#6b6b6b;
  --link:#8a8a8a;
  --rule:#8c8c8c;
  --header-bg:rgba(8,10,12,.85);
  --white:#ffffff;
  --btn:#2f7fd8;
  --footer-bg:#d9d9d9;
  --quote-mark:#c8c8c8;
  --night-deep:#101316;
  --night-mid:#2c3840;
  --mist:#6f8a99;
  --glow:#d8eefa;
}
*{margin:0;padding:0;box-sizing:border-box}
html,body{width:1200px;height:2724px;overflow:hidden;background:var(--white)}
body{position:relative;font-family:"Lato",Arial,sans-serif;color:var(--body)}

.hero{position:absolute;left:0;top:0;width:1200px;height:542px;
  background:
    radial-gradient(ellipse 120px 170px at 830px 400px,rgba(216,238,250,.95),rgba(216,238,250,0) 100%),
    radial-gradient(ellipse 330px 300px at 820px 380px,rgba(140,180,205,.75),rgba(90,125,145,.35) 55%,rgba(40,55,65,0) 100%),
    linear-gradient(180deg,rgba(16,19,22,.85) 0%,rgba(16,19,22,0) 35%,rgba(16,19,22,0) 70%,rgba(16,19,22,.9) 100%),
    linear-gradient(90deg,#17140f 0%,#3a352d 18%,#4a4c4a 38%,#5b7482 58%,#3b4e59 78%,#161c21 100%);}

.site-header{position:absolute;left:0;top:0;width:1200px;height:96px;background:var(--header-bg)}
.brand{position:absolute;left:168px;top:28px;color:var(--white)}
.brand-name{font-family:"Montserrat",sans-serif;font-weight:600;font-size:27px;line-height:1}
.brand-tag{font-size:17px;margin-top:5px}
.social{position:absolute;left:902px;top:28px;display:flex;gap:8px}
.social span{width:14px;height:14px;border-radius:50%;background:#e6e6e6}
.main-nav{position:absolute;left:744px;top:62px;display:flex;gap:32px;font-size:11px;color:var(--white)}
.main-nav a{color:inherit;text-decoration:none}
.main-nav .current{color:#bbbbbb}

.contact-strip{position:absolute;left:706px;top:554px}
.tel{font-family:"Montserrat",sans-serif;font-size:18px;color:var(--ink);font-weight:600}
.request-btn{display:block;margin-top:18px;margin-left:4px;width:180px;height:29px;border-radius:15px;background:var(--btn);
  color:var(--white);font-size:11px;font-weight:700;text-align:center;line-height:29px}

.content{position:absolute;left:180px;top:680px;width:975px}
h1{font-family:"Montserrat",sans-serif;font-weight:600;font-size:22px;color:var(--ink);margin-bottom:40px}
h2{font-family:"Montserrat",sans-serif;font-weight:600;font-size:18px;color:var(--ink);margin:0 0 20px}
.quote{position:relative;width:840px;padding:0 48px 0 0;margin-bottom:76px}
.quote::before{content:"\201C";position:absolute;left:0;top:-62px;font-size:84px;color:var(--quote-mark);font-family:Georgia,serif}
.quote::after{content:"\201D";position:absolute;right:0;bottom:-76px;font-size:84px;color:var(--quote-mark);font-family:Georgia,serif}
.quote p{font-style:italic;font-size:14px;line-height:1.6;color:var(--ink)}
.quote.lead p{font-weight:700}
.quote cite{display:block;text-align:right;font-size:9px;font-style:italic;color:var(--muted);margin-top:12px;padding-right:0}
.section{margin-top:-10px}
.section p{font-size:11.5px;line-height:19px;margin-bottom:22px}
.section a{color:var(--link);text-decoration:none}
.method{width:840px;border-top:2px solid var(--rule);padding:14px 0 0;margin-top:10px}
.method p{font-size:11px;line-height:1.75;margin:0}

.footer-cols{position:absolute;left:187px;top:1879px;width:833px;border-top:2px solid var(--rule)}
.col{position:absolute;top:26px;font-size:11px;line-height:23px}
.col a{color:var(--link);text-decoration:none}
.col-a{left:0;width:245px}
.col-b{left:288px;width:260px}
.col-c{left:571px;width:262px}
.col ul{list-style:none}
.col .gap{margin-top:20px}
.col .gap-lg{margin-top:38px}
.col .end-rule{border-top:2px solid var(--rule);margin-top:8px;width:240px}

.site-footer{position:absolute;left:0;top:2496px;width:1200px;height:228px;background:var(--footer-bg)}
.site-footer p{position:absolute;left:180px;top:58px;width:975px;font-size:11px;line-height:19px;color:var(--ink)}
.site-footer .copy{top:146px;left:0;width:1200px;text-align:center;color:#888}
.site-footer .top{top:180px;left:0;width:1200px;text-align:center;color:#888}
</style>
</head>
<body>
<div class="hero" role="img" aria-label="Photograph of a well dressed investigator standing in a dark misty alley holding a flashlight"></div>

<header class="site-header">
  <div class="brand">
    <div class="brand-name">Dorvale &amp; Kestrin ltd.</div>
    <div class="brand-tag">A Private Investigation And Analysis Firm</div>
  </div>
  <div class="social" aria-hidden="true"><span></span><span></span><span></span><span></span><span></span><span></span></div>
  <nav class="main-nav">
    <a class="current" href="#">Main</a>
    <a href="#"><b>Investigation &amp; Analysis</b></a>
    <a href="#"><b>News</b></a>
    <a href="#"><b>Fees</b></a>
  </nav>
</header>

<div class="contact-strip">
  <div class="tel">Tel. (555) 014-2739</div>
  <a class="request-btn">Submit Request For Service</a>
</div>

<main class="content">
  <h1>Ohio and West Virginia Private Investigators</h1>

  <blockquote class="quote lead">
    <p>Our experience and unbiased approach is your greatest strength! If you are an attorney, company, or private individual with a legal need we will provide you with accurate, timely and unbiased information that will help you make an informed decision, mitigate risk, and resolve problems.</p>
  </blockquote>

  <blockquote class="quote">
    <p>Dorvale &amp; Kestrin, Ltd. have been very helpful in our requests. Daniel is a very courteous and respectful person. Thanks for all you have done thus far!!! We will definitely use this firm in the future!!</p>
    <cite>— Harlan B. Tessmer, Attorney at Law, Tessmer Law Office - Riverbend, Ohio</cite>
  </blockquote>

  <blockquote class="quote">
    <p>Our Union recently hired Dorvale and Kestrin to conduct an investigation for us. The investigation concerned a certain high ranking official. The investigation entailed researching retrospectively over a course of several years. We found that Dorvale and Kestrin conducted a very thorough and accurate account of the information as requested. The report we were given was very professional, concise and satisfied our needs. The investigation was carried out and completed in a timely fashion assuring our union of the information we needed without undue costs.</p>
    <cite>— Lorna Vickery, President Union Local 4810</cite>
  </blockquote>

  <section class="section">
    <h2>What We Do</h2>
    <p>Dorvale &amp; Kestrin private investigators are available for immediate service in Ohio throughout the cities of Ironton, Portsmouth, Gallipolis, Jackson, Chillicothe, Cincinnati, Columbus, and surrounding areas. Service is immediately available in West Virginia throughout the cities of Huntington, Charleston, and surrounding areas.</p>
    <p>Private investigators are available to provide full support to attorneys involved in <a href="#">criminal defense</a> and <a href="#">civil litigation</a>. Full investigative support is available to the general public involving criminal and civil matters.</p>
    <p>Dorvale &amp; Kestrin private investigators are always easily obtainable for the general public. We keep our fees reasonable and never charge for travel. This makes us available to you without unnecessary expense. Investigative and analysis services are available by the hour or for a flat rate. <a href="#">Click here for our Fees.</a></p>
    <h2>Our Services</h2>
    <p>Private investigators are available for investigations involving <a href="#">Criminal Defense</a> and <a href="#">Legal Investigation</a>. We also provide <a href="#">Forensic Photography</a> services.</p>
    <h2>How Much Do We Charge</h2>
    <p>We believe the services of a private investigator should be obtainable and reasonable to the general public. The fees charged by Dorvale &amp; Kestrin are low compared to other similar firms. For one, we do not charge for travel. This makes us available to you without unnecessary expense. Investigative and analysis services are available by the hour or at a flat rate. See the <a href="#">private investigator fees</a> for more information.</p>
    <div class="method">
      <p>Our investigative and analysis ability is based on the application of Structured Analysis and Expert Judgement. The use of these methods allows us to provide clients of Dorvale &amp; Kestrin with objective results. In the areas of reconstructing past events, evaluating the credibility of evidence and witness testimony, processing of abstract information derived from multiple portals, and making analytical judgements based on available subject matter information. In turn, we are not only able to provide investigative service, but full analysis support to clients.</p>
    </div>
  </section>
</main>

<section class="footer-cols">
  <div class="col col-a">
    <p>Dorvale &amp; Kestrin was established with the view that private investigators should be the most highly trained and competent investigators available to the public. This expertise should surpass law enforcement standards of efficiency and rise to the level demonstrated by some of the most elite professional groups spread across the globe.</p>
    <ul class="gap-lg"><li><a href="#">Who We Are</a></li><li><a href="#">Founder and Owner</a></li></ul>
    <ul class="gap">
      <li>CRIMINAL DEFENSE TASKING</li>
      <li><a href="#">› Discovery File Review and Analysis</a></li>
      <li><a href="#">› Defendant Interview</a></li>
      <li><a href="#">› Crime Scene Review and Analysis</a></li>
      <li><a href="#">› Review and examination of physical evidence</a></li>
      <li><a href="#">› Discovery and Locating Witnesses</a></li>
      <li><a href="#">› Witness Interview</a></li>
      <li><a href="#">› Witness Background Check</a></li>
      <li><a href="#">› Alleged Victim Background Check</a></li>
      <li><a href="#">› Evidence Discovery</a></li>
      <li><a href="#">› Background Check of Expert Witness</a></li>
    </ul>
    <div class="end-rule"></div>
  </div>
  <div class="col col-b">
    <ul>
      <li>LEGAL INVESTIGATION</li>
      <li><a href="#">Legal Investigation</a></li>
      <li class="gap">LEGAL INVESTIGATION TASKING</li>
      <li><a href="#">› Discovery File Review and Analysis</a></li>
      <li><a href="#">› Discovery and Locating witnesses</a></li>
      <li><a href="#">› Witness Interview</a></li>
      <li><a href="#">› Witness Background Checks</a></li>
      <li class="gap"><a href="#">› Evidence Discovery</a></li>
      <li><a href="#">› Review and Examination of Physical Location or Physical Evidence</a></li>
      <li class="gap"><a href="#">Online Dating</a></li>
      <li><a href="#">Social Network Surveillance</a></li>
      <li class="gap">ANALYSIS OF INFORMATION</li>
      <li><a href="#">Analysis of Information</a></li>
      <li>› Application of Structured Analysis (Intelligence Analysis)</li>
      <li>› Discovery file analysis</li>
      <li>› Threat analysis (person, supply line, and physical structure)</li>
      <li>› Other assignments accepted on limited bases</li>
    </ul>
    <div class="end-rule"></div>
  </div>
  <div class="col col-c">
    <p>Perspective clients are highly encouraged to submit an <a href="#">electronic service inquiry</a>. After Dorvale &amp; Kestrin receives a perspective client's request, an investigator will contact the perspective client within twenty-four hours and provide a free consultation.</p>
    <p class="gap"><a href="#">Contact Dorvale &amp; Kestrin ltd.</a></p>
    <p class="gap">Mailing Address:<br><b>P.O. Box 417</b></p>
  </div>
</section>

<footer class="site-footer">
  <p>Dorvale &amp; Kestrin ltd. provides civil and criminal investigation services. Private investigators are available for immediate service in Ohio throughout the cities of Ironton, Portsmouth, Gallipolis, Jackson, Chillicothe, Cincinnati, Columbus, and surrounding areas. Service is immediately available in West Virginia throughout the cities of Huntington, Charleston, and surrounding areas.</p>
  <p class="copy">© 2012-2016 Dorvale &amp; Kestrin ltd. All rights reserved.</p>
  <p class="top">Start ^</p>
</footer>
</body>
</html>
```